New River III Precinct 6x11 GOTV postcard

We require BOTH persuasive copy and high-impact layout for an oversized 6x11 political mailer. This might be one person, but it likely requires a specialized "creative team." of an experienced political strategist copywriter PLUS a graphic designer - so the words fit the exact layout block, and the visuals reinforce the psychological punch of the headline.

The goal is to remove all excuses a targeted audience of ~900 registered Harvestline + ~1800 Unaffiliated voters in our precinct - have for not voting.

I need to be able to work by phone / online chat to iterate designs
I need to own the design in the top couple of software outputs that any printer service will require.

I want to experiment with very subtle background images as follows:
- Front of postcard that conveys "CHANGE" of not just seasons - but of encouraging change of precinct voter representation - so anything about fall foliage / conveyance of change tie-in is worthy of considering
- Back of postcard - any Appalachian long rage mountain view that includes 5-7 layers of hills in the distance.
Some photos as samples to consider.

Target Market(s)

~2,700 registered Harvestliners and Unaffiliated voters

Requirements
Must have
• We require BOTH persuasive copy and high-impact layout for an oversized 6x11 political mailer. This might be one person, but it likely requires a specialized "creative team." of an experienced political strategist copywriter PLUS a graphic designer - so the words fit the exact layout block, and the visuals reinforce the psychological punch of the headline
Nice to have
• subtle background photos

```html
<!DOCTYPE html>
<html lang="en">
<head>
<meta charset="utf-8">
<title>Vote for Change – Precinct Postcard</title>
<link rel="stylesheet" href="https://fonts.googleapis.com/css2?family=Oswald:wght@500;600&family=Open+Sans:ital,wght@0,400;0,700;1,700&display=swap">
<style>
:root{
  --red:#a51e24;
  --navy:#0e1744;
  --gold:#f0a81c;
  --rule:#e8a33a;
  --ink:#1c1c1c;
  --frame:#e8327a;
  --white:#ffffff;
}
*{box-sizing:border-box;margin:0;padding:0}
html,body{width:1200px;height:667px;overflow:hidden;background:#fff}
.postcard{position:relative;width:1200px;height:667px;border:1.5px solid var(--frame);background:#fff;font-family:"Open Sans",Arial,sans-serif;color:var(--ink)}
.headline-band{position:absolute;left:14px;top:14px;width:1173px;height:73px;background:var(--red);display:flex;align-items:center;justify-content:center;gap:30px;color:#fff;font-family:"Oswald",Impact,sans-serif;font-weight:600;font-size:31px;letter-spacing:-.2px}
.stars{display:flex;gap:7px}
.stars svg{width:22px;height:22px;fill:#fff}
.mountain-backdrop{position:absolute;left:14px;top:395px;width:1173px;height:201px;background:linear-gradient(180deg,#fff 0%,#d9e6ef 18%,#9fbdd3 45%,#4d7fa6 75%,#2e5f8a 100%)}
.panel{position:absolute;background:#fff;border:2px solid var(--navy);border-radius:16px;overflow:hidden}
.pain{left:43px;top:102px;width:391px;height:460px}
.pain-head{background:var(--navy);color:#fff;text-align:center;height:66px;padding-top:3px}
.pain-head h2{font-size:18.5px;font-weight:700;line-height:22px}
.pain-head h2 em{font-style:italic}
.pain-head p{font-size:10.6px;font-weight:700;line-height:13.4px}
.issue{display:flex;border-bottom:1.5px solid var(--rule);margin-left:69px;position:relative}
.issue:last-child{border-bottom:none}
.issue .icon{position:absolute;left:-64px;width:46px;height:46px;fill:var(--navy)}
.issue h3,.topic h3{font-family:"Oswald",Impact,sans-serif;font-weight:500;font-size:16px;color:var(--red);line-height:18px}
.issue-body{padding:6px 6px 4px 0;width:100%}
.issue p{font-size:13px;line-height:14.8px;letter-spacing:.5px;text-align:justify}
.topics{left:450px;top:104px;width:310px;height:460px}
.topic{margin:0 6px;padding:6px 6px 6px 4px;border-bottom:1.5px solid var(--rule)}
.topic:last-child{border-bottom:none}
.topic-title{display:flex;align-items:flex-end;gap:6px;margin-bottom:3px}
.topic-title svg{width:34px;height:32px;fill:var(--red)}
.topic p{font-size:13.2px;line-height:14.8px;text-align:justify}
.ballot{left:774px;top:102px;width:384px;height:462px}
.ballot-head{background:var(--navy);color:#fff;height:44px;display:flex;align-items:center;justify-content:center;font-family:"Oswald",Impact,sans-serif;font-weight:500;font-size:17px;padding-top:10px}
.ballot-list{list-style:none;padding:9px 10px 0 8px}
.ballot-list li{display:flex;align-items:baseline;height:26.7px;font-family:"Oswald",Impact,sans-serif;font-weight:500;font-size:12px;color:var(--navy);white-space:nowrap}
.ballot-list li::before{content:"★";color:var(--red);font-size:13px;margin-right:9px}
.ballot-list .leader{flex:1;border-bottom:1.6px dotted var(--navy);margin:0 3px;transform:translateY(-3px)}
.ballot-list .pick{color:var(--red)}
.footer-band{position:absolute;left:14px;top:596px;width:1173px;height:59px;background:var(--navy);display:flex;align-items:center;justify-content:center;gap:34px;font-family:"Oswald",Impact,sans-serif;font-weight:600;font-size:20px;letter-spacing:5.5px;color:#fff}
.footer-band .gold{color:var(--gold)}
.footer-band .red{color:#d42a2a}
.footer-band svg{width:20px;height:20px;fill:var(--gold)}
</style>
</head>
<body>
<svg width="0" height="0" style="position:absolute">
  <defs><symbol id="star" viewBox="0 0 24 24"><path d="M12 1l3.2 7.2 7.8.7-5.9 5.2 1.8 7.7L12 17.8 5.1 21.8l1.8-7.7L1 8.9l7.8-.7z"/></symbol></defs>
</svg>
<main class="postcard">
  <header class="headline-band">
    <span class="stars"><svg><use href="#star"/></svg><svg><use href="#star"/></svg><svg><use href="#star"/></svg></span>
    <h1 style="font:inherit">THIS NOVEMBER HOLD THEM ACCOUNTABLE – VOTE FOR CHANGE</h1>
    <span class="stars"><svg><use href="#star"/></svg><svg><use href="#star"/></svg><svg><use href="#star"/></svg></span>
  </header>

  <div class="mountain-backdrop" role="img" aria-label="Layered blue Appalachian mountain ridges fading into the distance"></div>

  <section class="panel pain">
    <div class="pain-head">
      <h2><em>INTENTIONAL</em> LOCAL PAIN</h2>
      <p>This is being delivered thanks to our current representative.<br>To avoid accountability, they’ve cleverly delayed many/most impacts<br>until AFTER the 2026 election.</p>
    </div>
    <div class="issue" style="height:60px">
      <svg class="icon" style="top:6px" viewBox="0 0 48 48"><circle cx="24" cy="11" r="6"/><circle cx="10" cy="14" r="5"/><circle cx="38" cy="14" r="5"/><path d="M14 38v-8a10 10 0 0120 0v8zM2 36v-6a8 8 0 0112-7 14 14 0 00-2 7v6zM46 36v-6a8 8 0 00-12-7 14 14 0 012 7v6z"/></svg>
      <div class="issue-body"><h3>FAMILY BUDGET</h3><p>exploded costs for everything: groceries, gas, car insurance, rent</p></div>
    </div>
    <div class="issue" style="height:106px">
      <svg class="icon" style="top:28px" viewBox="0 0 48 48"><circle cx="24" cy="24" r="20" fill="none" stroke="#0e1744" stroke-width="4"/><circle cx="24" cy="24" r="13"/><path d="M21 15h6v6h6v6h-6v6h-6v-6h-6v-6h6z" fill="#fff"/></svg>
      <div class="issue-body"><h3>HEALTH</h3><p>Expired subsidies, tax credits means 1 million families in NC will lose coverage or pay more. 50% cuts to hospitals, mental health facilities; rural facilities will be closing.</p></div>
    </div>
    <div class="issue" style="height:65px">
      <svg class="icon" style="top:2px" viewBox="0 0 48 48"><g fill="none" stroke="#0e1744" stroke-width="4.5"><circle cx="20" cy="22" r="10"/><path d="M27 15l12-12M30 3h9v9M20 32v14M14 40h12"/></g></svg>
      <div class="issue-body"><h3>REPRODUCTIVE RIGHTS</h3><p>Government authoritarian intrusion censor women’s rights</p></div>
    </div>
    <div class="issue" style="height:67px">
      <svg class="icon" style="top:10px" viewBox="0 0 48 48"><circle cx="24" cy="24" r="20" fill="none" stroke="#0e1744" stroke-width="4"/><path d="M15 12h2v8h2v-8h2v8h2v-8h1v10a4 4 0 01-3 4v12h-4V26a4 4 0 01-3-4V12zM29 12c4 0 5 6 5 12h-2v14h-4V12z"/></svg>
      <div class="issue-body"><h3>FOOD SECURITY</h3><p>Weaponized hunger – cuts to SNAP; school meals cut; additional work requirements.</p></div>
    </div>
    <div class="issue" style="height:88px">
      <svg class="icon" style="top:16px" viewBox="0 0 48 48"><path d="M24 4L2 13l22 9 16-6.5V26h3V14z"/><path d="M12 19v7c0 5 6 7 12 7s12-2 12-7v-7l-12 5z"/><path d="M6 48c0-9 8-13 18-13s18 4 18 13z"/></svg>
      <div class="issue-body"><h3>EDUCATION</h3><p>Watauga $2.2mm shortfall personnel cuts, freezesin hiring, teacher training. Abandoning civil rights of Special Ed students to HHS and DOL.</p></div>
    </div>
  </section>

  <section class="panel topics">
    <div class="topic" style="height:143px">
      <div class="topic-title"><svg viewBox="0 0 36 34"><path d="M18 2L2 16h4v16h24V16h4z"/><rect x="10" y="19" width="6" height="6" fill="#fff"/><rect x="20" y="19" width="6" height="6" fill="#fff"/></svg><h3>HOUSING</h3></div>
      <p>25% of renters are spending over 50% of incomeon rent. Especially bad locally; predatory leasingterms and skyrocketing rents. Proposed legislationis transforming HUD with the goal of getting rid of Section 8 housing that cares for vulnerablepopulations.</p>
    </div>
    <div class="topic" style="height:140px">
      <div class="topic-title"><svg viewBox="0 0 36 34"><circle cx="17" cy="17" r="14" fill="none" stroke="#a51e24" stroke-width="3"/><path d="M20 5l-9 14h6l-3 11 10-15h-6z"/></svg><h3>ENERGY</h3></div>
      <p>In 2022 Boone achieved 100% renewable energyin town buildings; this is now being destroyed by repeal of renewable energy project funding. Highland State Innovation District prepares renewable workforce rules – all this is now in limbo.</p>
    </div>
    <div class="topic">
      <div class="topic-title"><svg viewBox="0 0 36 34"><circle cx="17" cy="17" r="15"/><g fill="none" stroke="#fff" stroke-width="1.6"><ellipse cx="17" cy="17" rx="6" ry="15"/><path d="M2 17h30M5 9h24M5 25h24M17 2v30"/></g></svg><h3>ENVIRONMENT</h3></div>
      <p>Reduced protections from coal ash pond leaks threaten public health. Corporations not held responsible for damage; public picks up the tab. Environmental Justice enforcement no longer apriority. Logging in Watauga with no public oversight. It’s the “haz-mat” model: do nothing, wait for catastrophe, then fix it.</p>
    </div>
  </section>

  <section class="panel ballot">
    <h2 class="ballot-head">SAMPLE BALLOT RECOMMENDATIONS</h2>
    <ul class="ballot-list">
      <li>US SENATE<span class="leader"></span><span class="pick">RAY COLTER</span></li>
      <li>US HOUSE – DISTRICT 5<span class="leader"></span><span class="pick">CHET HOLLIS</span></li>
      <li>REQMT TO SHOW ID FOR VOTERS NOT IN PERSON<span class="leader"></span><span class="pick">No</span></li>
      <li>STATE SENATE – DISTRICT 47<span class="leader"></span><span class="pick">FRED HADLEY</span></li>
      <li>HOUSE OF REPS – DISTRICT 93<span class="leader"></span><span class="pick">CARL WESTON</span></li>
      <li>NC SUPREME COURT<span class="leader"></span><span class="pick">ALMA ELLERY</span></li>
      <li>NC COURT OF APPEALS – SEAT 1<span class="leader"></span><span class="pick">JON ASHWORTH</span></li>
      <li>NC COURT OF APPEALS – SEAT 2<span class="leader"></span><span class="pick">TONY HALVERS</span></li>
      <li>NC COURT OF APPEALS – SEAT 3<span class="leader"></span><span class="pick">CLARICE WALDEN</span></li>
      <li><span class="leader"></span></li>
      <li><span class="leader"></span></li>
      <li><span class="leader"></span></li>
      <li><span class="leader"></span></li>
      <li><span class="leader"></span></li>
      <li><span class="leader"></span></li>
    </ul>
  </section>

  <footer class="footer-band">
    <svg><use href="#star"/></svg>
    <p>OUR COMMUNITY. <span class="gold">OUR FUTURE.</span> <span class="red">OUR VOTE</span>.</p>
    <svg><use href="#star"/></svg>
  </footer>
</main>
</body>
</html>
```